IT Consulting Site Revamping for Marlune

I've put a skeleton together on my website, but realize I need some help (it's http://pilot.marlune-example.ca).
I've pulled together tidbits from other websites, but really need my site to be cleaned up, and really spruced up.
I primarily focus on the IT needs of small to medium size businesses, taking care of everything from their servers and networks down to their workstations.
I also want a page listing the vendors (and logos) that I work with including Quillsoft, Zentrix, Halvor, Brax, TL, RZO, VELK, Trevo, Gatemoor.
There should also be a simple form to get a quote that will email me.
The final design should communicate strength and reliability.
I would like this to be a fully functional website, that I can upload to Plumly Pages, with the same sort of pages that are existing on http://pilot.marlune-example.ca
Updates
Hey everyone,
Hi everyone,
Reason: Hi all,
There are some designers that would like to submit some new designs, so I'm extending the deadline.
Thanks,
Target Market(s)
Small to medium size business owners. This will primarily be males who work in the oil and gas industry.
Industry/Entity Type
Consulting
Look and feel
Each slider illustrates characteristics of the customer's brand and the style your logo design should communicate.

```html
<!DOCTYPE html>
<html lang="en">
<head>
<meta charset="utf-8">
<title>Marlune Solutions</title>
<link rel="stylesheet" href="https://fonts.googleapis.com/css2?family=Oswald:wght@300;400&family=PT+Sans&display=swap">
<style>
:root{
  --brand-blue:#2c5282;
  --nav-top:#2b4f86;
  --nav-bottom:#0b2448;
  --page-bg:#efefef;
  --hero-bg:#ececec;
  --strip-bg:#c9c9c9;
  --content-bg:#e4e4e4;
  --about-bg:#2c4f7d;
  --footer-bg:#03345f;
  --heading-grey:#444;
  --accent-blue:#0d4a9a;
  --light-blue:#5aaee8;
  --text-grey:#666;
  --white:#fff;
}
*{margin:0;padding:0;box-sizing:border-box}
html,body{width:1029px;height:1200px;overflow:hidden}
body{position:relative;background:var(--page-bg);font-family:Arial,Helvetica,sans-serif;color:var(--text-grey)}
.top-band{position:absolute;left:0;top:0;width:1029px;height:429px;background:var(--brand-blue)}
.brand{position:absolute;left:141px;top:16px;display:flex;align-items:center;gap:14px;color:var(--white)}
.brand-dot{width:82px;height:82px;border-radius:50%;background:var(--white)}
.brand-name{font-family:'PT Sans',sans-serif;font-size:58px;line-height:52px;letter-spacing:-1px}
.brand-sub{font-family:'PT Sans',sans-serif;font-size:13px;letter-spacing:11px;margin-top:2px}
.shell{position:absolute;left:88px;top:116px;width:860px;height:1063px;border-radius:14px;overflow:hidden;background:var(--content-bg);box-shadow:0 0 3px rgba(0,0,0,.4)}
.main-nav{height:54px;background:linear-gradient(var(--nav-top) 0,var(--nav-top) 45%,var(--nav-bottom) 55%,var(--nav-bottom) 100%);display:flex;justify-content:center;align-items:center;padding-bottom:6px}
.main-nav a{font-family:'PT Sans',sans-serif;color:var(--white);text-decoration:none;font-size:17px;padding:0 23px;border-left:1px solid rgba(255,255,255,.7);line-height:28px}
.main-nav a:first-child{border-left:none}
.hero{position:relative;height:274px;background:var(--hero-bg)}
.hero-title{position:absolute;left:66px;top:40px;font-family:Oswald,sans-serif;font-weight:300;text-transform:uppercase}
.hero-title .lead{display:block;color:var(--heading-grey);font-size:37px;line-height:41px}
.hero-title .claim{display:block;color:var(--accent-blue);font-size:49px;line-height:52px;margin-top:6px;font-weight:400}
.hero-art{position:absolute;left:542px;top:56px;width:245px;height:166px;background:radial-gradient(ellipse at center,#d6d6d6,#ececec 70%)}
.services{display:flex;height:146px;background:var(--strip-bg);padding:0 20px}
.service{flex:1;position:relative;padding:28px 10px 0 16px}
.service-dot{position:absolute;top:7px;width:16px;height:16px;border-radius:50%}
.service h3{font-family:Oswald,sans-serif;font-weight:300;font-size:19px;color:#333;text-transform:uppercase;line-height:24px;margin-bottom:6px;white-space:nowrap}
.service p{font-size:10.5px;line-height:12.4px;color:var(--text-grey);width:140px}
.service .more{position:absolute;bottom:12px;font-size:10.5px;font-style:italic;color:var(--text-grey);text-decoration:none}
.feature{position:relative;height:286px;background:linear-gradient(#e8e8e8,#dedede 80%,#ececec)}
.feature-copy{position:absolute;left:123px;top:30px;width:440px}
.feature-copy h2{font-family:Oswald,sans-serif;font-weight:300;font-size:19px;color:var(--light-blue);text-transform:uppercase;line-height:24px}
.feature-copy p{font-size:10.5px;line-height:12.4px;margin-bottom:12px}
.feature-art{position:absolute;left:598px;top:28px;width:146px;height:146px;background:radial-gradient(ellipse at center,#cfcfcf,#e2e2e2 70%)}
.about{position:relative;height:149px;background:var(--about-bg);color:var(--white)}
.about h2,.newsletter h2,.follow h2{font-family:Oswald,sans-serif;font-weight:300;font-size:19px;text-transform:uppercase;line-height:24px}
.about-copy{position:absolute;left:37px;top:14px;width:440px}
.about-copy p{font-size:10.5px;line-height:12.4px;margin-top:6px}
.newsletter{position:absolute;left:624px;top:14px}
.email-field{margin-top:10px;width:199px;height:28px;border:1px solid #7b94b8;background:#305686;color:var(--white);font-style:italic;font-size:10.5px;line-height:26px;padding-left:14px}
.subscribe{margin-top:21px;width:76px;height:28px;background:linear-gradient(#2b4f86,#0b2448);color:var(--white);font-style:italic;font-size:10.5px;line-height:28px;text-align:center;box-shadow:0 1px 2px rgba(0,0,0,.5)}
.site-footer{position:relative;height:154px;background:var(--footer-bg);color:var(--white)}
.footer-nav{position:absolute;left:40px;top:41px;display:flex;gap:34px}
.footer-nav a{color:var(--white);font-size:10.5px;text-decoration:none}
.copyright{position:absolute;left:44px;top:121px;font-size:10.5px;font-style:italic}
.follow{position:absolute;left:624px;top:18px}
.follow ul{list-style:none;margin-top:9px}
.follow li{display:flex;align-items:center;gap:19px;height:31px;font-size:10.5px}
.social-square{width:22px;height:22px;background:#3a8fd8;border-radius:2px}
</style>
</head>
<body>
<div class="top-band"></div>
<div class="brand">
  <div class="brand-dot"></div>
  <div><div class="brand-name">marlune</div><div class="brand-sub">solutions</div></div>
</div>
<div class="shell">
  <nav class="main-nav">
    <a href="#">HOME</a><a href="#">OUR SERVICES</a><a href="#">ABOUT US</a><a href="#">OUR PRODUCTS</a><a href="#">CONTACT US</a>
  </nav>
  <section class="hero">
    <h1 class="hero-title"><span class="lead">Small business information<br>technology services</span><span class="claim">Easy, affordable<br>and reliable.</span></h1>
    <div class="hero-art" role="img" aria-label="Illustration of a group of business figures in suits and ties"></div>
  </section>
  <section class="services">
    <div class="service"><span class="service-dot" style="left:86px;background:#5b8fc9"></span><h3>Managed IT Services</h3><p>Marlune is an IT outsourcing provider supplying small and medium sized businesses like yours with networking solutions, desktop services,</p><a class="more" href="#" style="left:100px">read more &gt;</a></div>
    <div class="service"><span class="service-dot" style="left:97px;background:#34507a"></span><h3>Storage and Virtualization</h3><p style="margin-left:24px">Marlune's Storage and Virtualization Services incorporate ongoing support, maintenance, operations and management of the ICT</p><a class="more" href="#" style="left:120px">read more &gt;</a></div>
    <div class="service"><span class="service-dot" style="left:75px;background:#0f2244"></span><h3 style="margin-left:22px">Networking</h3><p style="margin-left:2px">Marlune can help your small business keep your computer network under control. We are a complete network solution provider that focuses</p><a class="more" href="#" style="left:106px">read more &gt;</a></div>
    <div class="service"><span class="service-dot" style="left:88px;background:#64b6f5"></span><h3>Backup and Recovery</h3><p style="margin-left:8px">Your small business data is growing and data loss happens for many reasons. Hard drive crashes, viruses, hardware failure, fires,</p><a class="more" href="#" style="left:100px">read more &gt;</a></div>
  </section>
  <section class="feature">
    <div class="feature-copy">
      <h2>Spyware and Virus Removal</h2>
      <p>Malicious Code has become increasingly complex and infections involve more system elements than ever before. Marlune has tools to automatically conduct what would often amount to extensive and tedious manual removal tasks. If your system has become infected with a virus or spyware, make sure you call us before is too late. We offer a Spyware and Virus Removal service. Sit back and let an expert scan and clear your PC of spyware and viruses.</p>
      <h2 style="margin-top:6px">On Site Computer Repair Service</h2>
      <p>For over 30 years, Norvik has been the trusted technology partner for computer repair and IT technical support for many small businesses like yours across Ireland. Whether your computer is infected with a virus, spyware, data recovery, or you are looking for an IT company to help you manage your small business IT systems, Norvik is here to help you.</p>
      <p>The Norvik on-site computer service is fast, reliable and affordable. Our computer network engineers and computer technicians can come to your small business to solve any computer problem you may be experiencing. Our standard business support response time is 1-2 hrs.</p>
    </div>
    <div class="feature-art" role="img" aria-label="Illustration of two business figures, one holding a briefcase and one a life ring"></div>
  </section>
  <section class="about">
    <div class="about-copy">
      <h2>Shortly about us</h2>
      <p>Marlune Solutions is a computer solutions provider and IT consulting firm that supports a wide variety of local small businesses in the Calgary area primarily. Our company also provides IT services to businesses throughout Alberta on special projects.</p>
      <p style="margin-top:12px">Marlune has been trusted for over the last 7 years by small business companies like yours. Whether you are looking for an ongoing computer support company, looking to outsource your small business computer work, or just looking for a computer company to help you solve a computer problem, Marlune is your right choice.</p>
    </div>
    <div class="newsletter">
      <h2>Newsletter</h2>
      <div class="email-field">your email</div>
      <div class="subscribe">Subscribe</div>
    </div>
  </section>
  <footer class="site-footer">
    <nav class="footer-nav"><a href="#">Home</a><a href="#">Our Services</a><a href="#">About us</a><a href="#">Our Products</a><a href="#">Contact us</a></nav>
    <div class="copyright">Marlune solutions © 2012 | Privacy Policy</div>
    <div class="follow">
      <h2>Follow us</h2>
      <ul>
        <li><span class="social-square"></span>Follow us on Chirply</li>
        <li><span class="social-square"></span>Join us on Friendbook</li>
        <li><span class="social-square"></span>Subscribe to our blog</li>
      </ul>
    </div>
  </footer>
</div>
</body>
</html>
```